Healthcare patient advocacy company needs banner for conference booth

We need a banner to hang behind us in our booth at conferences. I would like something that prominently features our company name - velorin LLC. And also includes the following language: No employee should face medical debt alone. No Plan should be unrepresented. Expert advocacy and legal support from first bill to final resolution. The colors we use for our other materials are HEX 002C45, FECC73, 00C6CF, E0D5B9, 004C66. And the font is Epilogue. I would welcome some graphics, but no scales of justice or dollar bills or anything like that. I'm attaching some materials so you can see one of our brochures.

Target Market(s)

B2B - health insurers, third-party health care administrators, cost-containment companies

Industry/Entity Type

Healthcare Advocacy

Requirements
Must have
• Name prominently displayed and taglines in project description.
Nice to have
• I would like something easy to read and eye-catching that is not overly complicated or cutsey.
Should not have
• Scales of justice or dollar signs.

```html
<!DOCTYPE html>
<html lang="en">
<head>
<meta charset="utf-8">
<title>velorin LLC – Booth Banner</title>
<link rel="stylesheet" href="https://fonts.googleapis.com/css2?family=Epilogue:wght@400;500;700&family=Roboto+Condensed:wght@700&display=swap">
<style>
  :root {
    --navy-deep: #002C45;
    --navy-mid: #004C66;
    --navy-ink: #0d2347;
    --gold: #FECC73;
    --gold-warm: #f2b24f;
    --teal: #00C6CF;
    --teal-light: #8fdbe6;
    --sand: #E0D5B9;
    --cream: #f6f0e2;
    --stage: #b3b3b3;
  }
  * { margin: 0; padding: 0; box-sizing: border-box; }
  html, body { width: 706px; height: 1200px; overflow: hidden; }
  body {
    background: var(--stage);
    font-family: "Epilogue", sans-serif;
    position: relative;
  }
  .banner {
    position: absolute;
    left: 23px;
    top: 336px;
    width: 660px;
    height: 527px;
    overflow: hidden;
    background: linear-gradient(160deg, #1b3a6e 0%, var(--navy-ink) 45%, #0a1b3a 100%);
  }
  .banner-art { position: absolute; inset: 0; width: 100%; height: 100%; }
  .brand-name {
    position: absolute;
    top: 30px;
    left: 0;
    width: 100%;
    text-align: center;
    font-family: "Epilogue", sans-serif;
    font-weight: 700;
    font-size: 52px;
    line-height: 1;
    color: var(--gold);
    letter-spacing: -0.5px;
  }
  .divider {
    position: absolute;
    top: 101px;
    left: 40px;
    width: 583px;
    height: 1px;
    background: var(--cream);
    opacity: 0.85;
  }
  .headline {
    position: absolute;
    top: 118px;
    left: 0;
    width: 100%;
    text-align: center;
    font-family: "Roboto Condensed", sans-serif;
    font-weight: 700;
    font-size: 40px;
    line-height: 35px;
    color: var(--cream);
    text-transform: uppercase;
  }
  .tagline-band {
    position: absolute;
    top: 200px;
    left: 134px;
    width: 391px;
    height: 31px;
    background: linear-gradient(90deg, var(--teal) 0%, var(--teal-light) 50%, var(--teal) 100%);
    display: flex;
    align-items: center;
    justify-content: center;
    font-family: "Roboto Condensed", sans-serif;
    font-weight: 700;
    font-size: 23px;
    color: var(--navy-deep);
    text-transform: uppercase;
  }
  .subline {
    position: absolute;
    top: 243px;
    left: 0;
    width: 100%;
    text-align: center;
    font-size: 14px;
    font-weight: 400;
    color: var(--cream);
  }
  .web-icon {
    position: absolute;
    left: 169px;
    top: 450px;
    width: 26px;
    height: 26px;
  }
  .web-address {
    position: absolute;
    left: 60px;
    top: 481px;
    width: 268px;
    text-align: center;
    font-size: 17px;
    font-weight: 400;
    color: #ffffff;
  }
  .web-address strong { font-weight: 700; }
</style>
</head>
<body>
  <section class="banner" aria-label="velorin LLC conference booth banner">
    <svg class="banner-art" viewBox="0 0 660 527" preserveAspectRatio="none" aria-hidden="false">
      <defs>
        <linearGradient id="backdropTone" x1="0" y1="0" x2="1" y2="1">
          <stop offset="0" stop-color="#23457d" stop-opacity="0.55"/>
          <stop offset="0.6" stop-color="#0d2347" stop-opacity="0"/>
        </linearGradient>
        <linearGradient id="photoTone" x1="0" y1="0" x2="1" y2="0">
          <stop offset="0" stop-color="#d9822c"/>
          <stop offset="0.2" stop-color="#c97a30"/>
          <stop offset="0.32" stop-color="#e8ecf3"/>
          <stop offset="0.45" stop-color="#3f7cc6"/>
          <stop offset="0.58" stop-color="#f1f3f7"/>
          <stop offset="0.75" stop-color="#c7ccd6"/>
          <stop offset="1" stop-color="#6f7a8c"/>
        </linearGradient>
        <linearGradient id="goldBand" x1="0" y1="0" x2="1" y2="0">
          <stop offset="0" stop-color="#f5b954"/>
          <stop offset="0.35" stop-color="#FECC73"/>
          <stop offset="0.7" stop-color="#f7bf5c"/>
          <stop offset="1" stop-color="#FECC73"/>
        </linearGradient>
        <linearGradient id="footerTone" x1="0" y1="0" x2="1" y2="0">
          <stop offset="0" stop-color="#0b1f45"/>
          <stop offset="1" stop-color="#0a1c3e"/>
        </linearGradient>
      </defs>

      <rect class="backdrop-photo" role="img" aria-label="Faint photo of a health insurance claim form and stethoscope" x="0" y="0" width="660" height="330" fill="url(#backdropTone)"/>

      <path class="photo-area" role="img" aria-label="Photo of a doctor in a white coat writing on a clipboard while consulting a patient"
            d="M0,322 C160,372 320,302 480,292 C570,286 620,304 660,326 L660,527 L0,527 Z" fill="url(#photoTone)"/>

      <path class="gold-wave"
            d="M0,292 C160,342 320,285 480,276 C570,271 620,298 660,320 L660,330 C620,308 570,290 480,292 C320,305 160,370 0,330 Z"
            fill="url(#goldBand)"/>

      <path class="footer-wave"
            d="M0,448 C60,424 120,416 185,428 C300,452 420,522 560,512 C610,508 640,494 660,482 L660,527 L0,527 Z"
            fill="url(#footerTone)"/>
      <path class="footer-accent"
            d="M0,470 C30,448 70,436 110,438 C70,452 50,490 60,527 L0,527 Z" fill="#1f6fd0" opacity="0.85"/>
      <path class="footer-accent-light"
            d="M20,527 C20,490 45,458 95,442 C70,470 62,500 70,527 Z" fill="#29a8ea" opacity="0.7"/>
    </svg>

    <h1 class="brand-name">velorin LLC</h1>
    <div class="divider"></div>
    <h2 class="headline">No employee should face<br>medical debt alone.</h2>
    <p class="tagline-band">No plan should be unrepresented</p>
    <p class="subline">Expert advocacy and legal support from first bill to final resolution.</p>

    <svg class="web-icon" viewBox="0 0 26 26" aria-hidden="true">
      <circle cx="13" cy="13" r="13" fill="var(--gold)"/>
      <g fill="none" stroke="var(--navy-deep)" stroke-width="1.2">
        <circle cx="13" cy="13" r="7"/>
        <ellipse cx="13" cy="13" rx="3" ry="7"/>
        <line x1="6" y1="13" x2="20" y2="13"/>
        <line x1="7" y1="9.5" x2="19" y2="9.5"/>
        <line x1="7" y1="16.5" x2="19" y2="16.5"/>
      </g>
    </svg>
    <p class="web-address">www.<strong>velorinhealth</strong>.com</p>
  </section>
</body>
</html>
```